Ministy Website or Church Website

I need a basic ministry website. The pages I need, Homepage or landing page, a contact page. services offered page, I need an about page, I need a donation page

```html
<!DOCTYPE html>
<html lang="en">
<head>
<meta charset="utf-8">
<title>Gracefield Church</title>
<link href="https://fonts.googleapis.com/css2?family=Roboto+Slab:wght@300;400;500;600;700&family=Lora:wght@400;500&display=swap" rel="stylesheet">
<style>
:root{
  --gold:#cbb27a;
  --gold-soft:#e4d6b2;
  --ink:#111111;
  --text:#2a2a2a;
  --muted:#8a8a8a;
  --panel:#f3f3f3;
  --line:#dcdcdc;
  --white:#ffffff;
  --star:#f2a818;
}
*{box-sizing:border-box;margin:0;padding:0}
html,body{width:1200px;height:4735px;overflow:hidden}
body{position:relative;background:var(--white);font-family:"Lora",serif;color:var(--text)}
.abs{position:absolute}
h1,h2,h3,h4,.slab{font-family:"Roboto Slab",serif}
.photo{position:absolute}

/* header + hero */
.hero{position:absolute;left:0;top:0;width:1200px;height:438px;background:linear-gradient(180deg,#2b2622 0%,#3d352d 45%,#1a1714 100%)}
.hero-shade{position:absolute;inset:0;background:rgba(0,0,0,.35)}
.nav{position:absolute;left:0;top:0;width:1200px;height:60px}
.brand{position:absolute;left:30px;top:18px;display:flex;align-items:center;gap:7px;font-family:"Roboto Slab",serif;font-weight:600;font-size:15px;color:var(--white)}
.brand i{width:14px;height:14px;background:var(--gold);display:block}
.menu{position:absolute;left:378px;top:23px;display:flex;gap:14px;font-family:"Roboto Slab",serif;font-size:10px;color:var(--white);letter-spacing:.3px}
.search{position:absolute;left:1040px;top:22px}
.donate{position:absolute;left:1094px;top:0;width:106px;height:60px;background:var(--gold);color:var(--white);font-family:"Roboto Slab",serif;font-size:10px;display:flex;align-items:center;justify-content:center}
.hero-title{position:absolute;left:0;width:1200px;top:128px;text-align:center;font-size:40px;font-weight:600;color:var(--white)}
.hero-title span{color:var(--gold)}
.hero-text{position:absolute;left:380px;width:440px;top:220px;text-align:center;font-size:10px;line-height:20px;color:#e4e4e4}
.btn{background:var(--gold);color:var(--ink);font-family:"Roboto Slab",serif;font-size:10px;display:flex;align-items:center;justify-content:center}
.hero-btn{position:absolute;left:515px;top:289px;width:170px;height:33px}
.arrow-box{position:absolute;top:203px;width:30px;height:30px;border:1.5px solid var(--white);display:flex;align-items:center;justify-content:center}

/* history */
.section-title{font-family:"Roboto Slab",serif;font-weight:600;color:var(--ink)}
.center{text-align:center}
.small{font-size:10px;line-height:20px;color:var(--muted)}
.partner{position:absolute;top:700px;width:96px;height:22px;border-radius:2px;background:#d7d7d7}

/* video */
.video-band{position:absolute;left:0;top:768px;width:1200px;height:362px;background:linear-gradient(135deg,#6b4f3a 0%,#c9b7a0 40%,#7a5f48 70%,#3a2a20 100%)}
.player{position:absolute;left:252px;top:933px;width:698px;height:62px;background:rgba(30,30,30,.75)}

/* gallery */
.tile{position:absolute;width:220px}
.ministry-card{position:absolute;left:254px;top:1292px;width:220px;height:309px;border:5px solid var(--gold);background:linear-gradient(180deg,#4a4540,#2a2622)}

/* pastor */
.panel{position:absolute;left:0;width:1200px;background:var(--panel)}
.check{display:flex;align-items:center;gap:10px;font-size:10px;color:var(--muted);line-height:18px}
.check i{width:9px;height:9px;border:1px solid var(--gold);border-radius:50%;display:block}

/* reviews */
.round-btn{position:absolute;width:26px;height:26px;border-radius:50%;background:var(--gold);display:flex;align-items:center;justify-content:center}
.review{position:absolute;top:3760px;width:210px}
.stars{color:var(--star);font-size:13px;letter-spacing:2px}
.review h4{font-size:12px;font-weight:600;color:var(--ink);margin:4px 0 6px}
.review p{font-size:10px;line-height:17px;color:var(--muted)}
.who{display:flex;align-items:center;gap:10px;margin-top:10px}
.avatar{width:34px;height:34px;border-radius:50%;background:#8c7a6a}
.who b{display:block;font-size:11px;color:var(--gold);font-weight:400}
.who span{font-size:8px;color:var(--ink)}
.ghost{position:absolute;font-family:"Roboto Slab",serif;font-weight:700;font-size:70px;color:rgba(0,0,0,.05);white-space:nowrap}

/* events */
.event{position:absolute;top:4088px;width:220px}
.event .img{height:187px}
.event h4{font-size:11px;font-weight:600;color:var(--ink);margin-top:20px}
.meta{font-size:7px;color:var(--muted);margin-top:10px;display:flex;gap:12px;align-items:center}
.meta i{width:7px;height:7px;border-radius:50%;border:1px solid var(--gold);display:inline-block;margin-right:5px}

/* footer */
.cta{position:absolute;left:0;top:4389px;width:1200px;height:73px;background:var(--gold)}
.footer-col h4{font-size:13px;font-weight:600;color:var(--ink);margin-bottom:14px}
.footer-col p,.footer-col li{font-size:9px;line-height:16px;color:var(--muted);list-style:none}
.field{border-bottom:1px solid #333;height:24px;font-size:8px;color:var(--ink);display:flex;justify-content:space-between;align-items:flex-end;padding-bottom:4px;margin-bottom:14px}
.social{width:22px;height:22px;border-radius:50%;border:1px solid #bbb;display:inline-block;margin-right:9px}
</style>
</head>
<body>

<!-- HERO -->
<header class="hero" role="img" aria-label="Church interior with rows of wooden pews">
  <div class="hero-shade"></div>
</header>
<nav class="nav">
  <div class="brand"><i></i>Gracefield Church</div>
  <div class="menu"><span>HOME ▾</span><span>MINISTRIES ▾</span><span>SERMONES ▾</span><span>EVENTS ▾</span><span>BLOG ▾</span><span>SERVICES ▾</span><span>PAGES ▾</span></div>
  <svg class="search" width="12" height="12" viewBox="0 0 12 12"><circle cx="5" cy="5" r="3.8" fill="none" stroke="#fff" stroke-width="1.3"/><line x1="8" y1="8" x2="11" y2="11" stroke="#fff" stroke-width="1.3"/></svg>
  <div class="donate">DONATE</div>
</nav>
<h1 class="hero-title">We Belive In <span>The God</span> Grace</h1>
<p class="hero-text">god cannot be realized through the intellect. intellect can lead one to a certain extent and no further. it is a matter of faith and experience derived from that faith.</p>
<div class="btn hero-btn">CONNECT WITH US</div>
<div class="arrow-box" style="left:18px"><svg width="14" height="10" viewBox="0 0 14 10"><path d="M13 5H2M5 1L1 5l4 4" fill="none" stroke="#fff" stroke-width="1.4"/></svg></div>
<div class="arrow-box" style="left:1152px"><svg width="14" height="10" viewBox="0 0 14 10"><path d="M1 5h11M9 1l4 4-4 4" fill="none" stroke="#fff" stroke-width="1.4"/></svg></div>
<svg class="abs" style="left:588px;top:390px" width="24" height="36" viewBox="0 0 24 36"><rect x="1" y="1" width="22" height="34" rx="11" fill="none" stroke="#fff" stroke-width="1.5"/><line x1="12" y1="8" x2="12" y2="15" stroke="#fff" stroke-width="1.5"/></svg>

<!-- HISTORY -->
<svg class="abs" style="left:586px;top:450px" width="28" height="150" viewBox="0 0 28 150"><rect x="10" y="0" width="8" height="150" fill="var(--gold-soft)" opacity=".5"/><rect x="0" y="30" width="28" height="8" fill="var(--gold-soft)" opacity=".5"/></svg>
<svg class="abs" style="left:310px;top:500px" width="14" height="10" viewBox="0 0 14 10"><path d="M13 5H2M5 1L1 5l4 4" fill="none" stroke="#111" stroke-width="1.4"/></svg>
<svg class="abs" style="left:874px;top:500px" width="14" height="10" viewBox="0 0 14 10"><path d="M1 5h11M9 1l4 4-4 4" fill="none" stroke="#111" stroke-width="1.4"/></svg>
<h2 class="abs section-title center" style="left:0;width:1200px;top:485px;font-size:24px">Our Church History</h2>
<p class="abs small center" style="left:340px;width:520px;top:530px">lorem ipsum dolor sit amet, consectetur adipiscing elit, sed do eiusmod tempor incididunt ut labore et dolore magna aliqua. ut enim ad minim veniam, quis nostrud exercitation ullamco laboris nisi ut aliquip ex ea commodo consequat.</p>
<p class="abs center" style="left:0;width:1200px;top:597px;font-size:9px;color:var(--gold)">2020</p>
<p class="abs center slab" style="left:0;width:1200px;top:615px;font-size:9px;font-weight:600;color:var(--ink)">5k Members</p>
<div class="abs" style="left:248px;top:650px;width:704px;height:1px;background:var(--line)"></div>
<div class="partner" style="left:254px"></div>
<div class="partner" style="left:400px"></div>
<div class="partner" style="left:552px"></div>
<div class="partner" style="left:700px"></div>
<div class="partner" style="left:852px"></div>

<!-- VIDEO -->
<div class="video-band" role="img" aria-label="Clergy in white robes reading during a service"></div>
<div class="player">
  <p class="abs slab" style="left:20px;top:16px;font-size:12px;font-weight:600;color:#fff">Combined With A Handful</p>
  <p class="abs" style="left:20px;top:36px;font-size:9px;color:#ddd">Lorem Ipsum Dolor Sit Amet, Consectetur</p>
  <svg class="abs" style="left:366px;top:23px" width="14" height="16" viewBox="0 0 14 16"><path d="M1 1l12 7-12 7z" fill="#fff"/></svg>
  <span class="abs" style="left:402px;top:26px;font-size:7px;color:#fff">0:00</span>
  <div class="abs" style="left:422px;top:30px;width:206px;height:2px;background:#fff"></div>
</div>

<!-- OUR CHURCH + GALLERY -->
<svg class="abs" style="left:618px;top:1160px" width="22" height="100" viewBox="0 0 22 100"><rect x="8" y="0" width="6" height="100" fill="var(--gold-soft)" opacity=".5"/><rect x="0" y="22" width="22" height="6" fill="var(--gold-soft)" opacity=".5"/></svg>
<p class="abs slab center" style="left:0;width:1200px;top:1180px;font-size:11px;font-weight:600;color:var(--ink)">Our Church</p>
<p class="abs slab center" style="left:240px;width:720px;top:1198px;font-size:22px;line-height:31px;color:var(--ink)">“What i like about Church is that it create a way of seeing the world in the light of God.”</p>

<div class="ministry-card">
  <svg class="abs" style="left:86px;top:36px" width="36" height="36" viewBox="0 0 36 36"><rect x="15" y="0" width="6" height="36" fill="var(--gold)"/><rect x="0" y="15" width="36" height="6" fill="var(--gold)"/></svg>
  <p class="abs slab center" style="left:0;width:210px;top:180px;font-size:11px;color:var(--gold)">Church Life</p>
  <p class="abs slab center" style="left:0;width:210px;top:200px;font-size:22px;font-weight:600;color:var(--gold)">Ministries</p>
  <p class="abs center" style="left:30px;width:150px;top:236px;font-size:9px;line-height:13px;color:#eee">Lorem Ipsum Dolor Sit Amet, Consectetur</p>
</div>
<div class="photo" style="left:254px;top:1621px;width:220px;height:313px;background:linear-gradient(180deg,#ece9e6,#bdb6ae)" role="img" aria-label="Person holding a hand-lettered sign outdoors"></div>
<div class="photo" style="left:254px;top:1950px;width:220px;height:239px;background:linear-gradient(135deg,#f2b24a,#7d8a3c 60%,#3f4a22)" role="img" aria-label="Two children reading a book in a sunlit field"></div>
<div class="photo" style="left:254px;top:2210px;width:220px;height:312px;background:linear-gradient(180deg,#8fb0d6,#dfe8f2)" role="img" aria-label="Wooden cross against a cloudy sky"></div>

<div class="photo" style="left:492px;top:1290px;width:220px;height:156px;background:linear-gradient(135deg,#1c4a66,#4f8fb0)" role="img" aria-label="Swimmer holding a cross in the water"></div>
<div class="photo" style="left:492px;top:1465px;width:220px;height:156px;background:linear-gradient(135deg,#c5c7c2,#6f746c)" role="img" aria-label="Crucifix statue on a wall"></div>
<div class="photo" style="left:492px;top:1638px;width:220px;height:204px;background:radial-gradient(circle at 70% 35%,#f8f6e6,#3a6ea8 45%,#142a4a)" role="img" aria-label="Hand reaching toward the sun in a blue sky"></div>
<div class="photo" style="left:492px;top:1856px;width:220px;height:270px;background:linear-gradient(180deg,#0c0c0c,#2b2520)" role="img" aria-label="Procession with candles and a cross at night"></div>
<div class="photo" style="left:492px;top:2145px;width:220px;height:206px;background:radial-gradient(ellipse at 50% 20%,#d8d8d8,#3a3a3a 60%,#111)" role="img" aria-label="Figure standing in a beam of light"></div>
<div class="photo" style="left:492px;top:2366px;width:220px;height:156px;background:linear-gradient(180deg,#cfcfcf,#6b6b6b)" role="img" aria-label="Person standing before large painted wall letters"></div>

<div class="photo" style="left:730px;top:1290px;width:220px;height:204px;background:linear-gradient(135deg,#8a9bb1,#3f5a80 60%,#6a5544)" role="img" aria-label="Person kneeling with an open bible"></div>
<div class="photo" style="left:730px;top:1507px;width:220px;height:204px;background:linear-gradient(180deg,#3f6f95,#24496a)" role="img" aria-label="Man praying among church pews"></div>
<div class="photo" style="left:730px;top:1724px;width:220px;height:160px;background:linear-gradient(135deg,#e9e3d6,#c98f1f 70%)" role="img" aria-label="Hand holding up a bible"></div>
<div class="photo" style="left:730px;top:1899px;width:220px;height:198px;background:linear-gradient(180deg,#5c9fd8,#cfe3f4)" role="img" aria-label="Person raising a flag under a blue sky"></div>
<div class="photo" style="left:730px;top:2116px;width:220px;height:194px;background:linear-gradient(135deg,#e8b060,#6f7f3a 65%,#39431f)" role="img" aria-label="Woman praying in a sunlit park"></div>
<div class="photo" style="left:730px;top:2329px;width:220px;height:193px;background:linear-gradient(135deg,#e8ddc8,#8b6a48 50%,#3a2a1c)" role="img" aria-label="Crucifix beside a bright window"></div>

<!-- PASTOR -->
<section class="panel" style="top:2568px;height:487px"></section>
<div class="photo" style="left:254px;top:2619px;width:280px;height:390px;background:linear-gradient(180deg,#c79d80 0%,#a8806a 30%,#181818 45%,#0d0d0d 100%)" role="img" aria-label="Man in a black shirt wearing a cross necklace"></div>
<h2 class="abs section-title" style="left:558px;top:2650px;font-size:25px">Marcus Ellory</h2>
<div class="abs" style="left:558px;top:2698px;width:2px;height:46px;background:var(--gold)"></div>
<p class="abs small" style="left:580px;top:2695px;width:370px;line-height:18px">Worship is a way of feeling, of touching, of loving. What you have caught on film is captured forever.. It remembers little things, long after you have forgotten everything.</p>
<h4 class="abs slab" style="left:558px;top:2765px;font-size:12px;font-weight:600;color:var(--ink)">A Short Story About Me</h4>
<p class="abs small" style="left:558px;top:2783px;width:445px;line-height:18px">Maecenas non faucibus nibh. Duis et eleifend sem, ut venenatis quam. Pelle ntesqueeu quam ac arcu elementum vestibulum quis eu nulla. Donec lacinia risus ac ex mollis, sed faucibus magna pellentesque. Praesent volutpat mi ut leo vehicula, iaculis finibus leo fermentum.</p>
<h4 class="abs slab" style="left:558px;top:2853px;font-size:12px;font-weight:600;color:var(--ink)">Why Choose My Church?</h4>
<div class="abs" style="left:558px;top:2874px">
  <div class="check"><i></i>Aenean vehicula molestie aliquet. Maecenas sed pretium.</div>
  <div class="check"><i></i>Nulla malesuada id ipsum quis vestibulum. In in sapien</div>
  <div class="check"><i></i>Fringilla, gravida nisl sit amet, consequat turpis.</div>
  <div class="check"><i></i>Praesent at gravida dolor. Duis tristique sit amet lacus</div>
  <div class="check"><i></i>Nulla malesuada id ipsum quis vestibulum. In in sapien</div>
</div>

<!-- LIVE SERMON -->
<div class="ghost" style="left:345px;top:3080px">My Own Style</div>
<h2 class="abs section-title center" style="left:0;width:1200px;top:3108px;font-size:24px">Live Sermon</h2>
<p class="abs small center" style="left:360px;width:480px;top:3142px;line-height:17px">Maecenas non faucibus nibh. Duis et eleifend sem, ut venenatis quam. Pelle ntesque eu quam ac arcu elementum vestibulum quis eu nulla. Donec lacinia risus ac ex molli</p>
<div class="abs" style="left:307px;top:3202px;width:586px;height:364px;background:#0a0a0a"></div>
<div class="photo" style="left:319px;top:3214px;width:562px;height:340px;background:radial-gradient(ellipse at 40% 50%,#d9c9a2,#8a5a2a 45%,#2a1a10)" role="img" aria-label="Priest in an embroidered robe at an altar with candles"></div>

<!-- REVIEWS -->
<section class="panel" style="top:3612px;height:364px"></section>
<div class="ghost" style="left:246px;top:3622px">Our Reviews</div>
<h2 class="abs section-title" style="left:326px;top:3660px;font-size:24px">What Our Member Says</h2>
<div class="round-btn" style="left:894px;top:3661px"><svg width="12" height="10" viewBox="0 0 12 10"><path d="M1 5h9M7 2l3 3-3 3" fill="none" stroke="#111" stroke-width="1.3"/></svg></div>
<div class="round-btn" style="left:926px;top:3661px"><svg width="12" height="10" viewBox="0 0 12 10"><path d="M11 5H2M5 2L2 5l3 3" fill="none" stroke="#111" stroke-width="1.3"/></svg></div>
<div class="abs" style="left:254px;top:3712px;width:696px;height:1px;background:var(--line)"></div>

<div class="review" style="left:254px"><div class="stars">★★★★★</div><h4 class="slab">“Thet're Exactly In Mind”</h4><p>"Lorem ipsum dolor sit amet, consectetur adipiscing elit, sed do eiusmod tempor in cididunt ut labore et dolore magna aliqua Ut enim ad minim veniam,</p><div class="who"><div class="avatar" role="img" aria-label="Member portrait"></div><div><b>Jane</b><span>CEO, Abc Company</span></div></div></div>
<div class="review" style="left:500px"><div class="stars">★★★★★</div><h4 class="slab">Loved It</h4><p>"Lorem ipsum dolor sit amet, consectetur adipiscing elit, sed do eiusmod tempor in cididunt ut labore et dolore magna aliqua Ut enim ad minim veniam,</p><div class="who"><div class="avatar" role="img" aria-label="Member portrait"></div><div><b>Daniel Roe</b><span>CEO, Abc Company</span></div></div></div>
<div class="review" style="left:745px"><div class="stars">★★★★★</div><h4 class="slab">He Is The Best</h4><p>"Lorem ipsum dolor sit amet, consectetur adipiscing elit, sed do eiusmod tempor in cididunt ut labore et dolore magna aliqua Ut enim ad minim veniam,</p><div class="who"><div class="avatar" role="img" aria-label="Member portrait"></div><div><b>Jessa</b><span>CEO, Abc Company</span></div></div></div>

<!-- EVENTS -->
<div class="ghost" style="left:246px;top:3995px">News &amp; Blog</div>
<h2 class="abs section-title" style="left:326px;top:4033px;font-size:24px">Upcoming Event</h2>
<div class="round-btn" style="left:894px;top:4033px"><svg width="12" height="10" viewBox="0 0 12 10"><path d="M1 5h9M7 2l3 3-3 3" fill="none" stroke="#111" stroke-width="1.3"/></svg></div>
<div class="round-btn" style="left:926px;top:4033px"><svg width="12" height="10" viewBox="0 0 12 10"><path d="M11 5H2M5 2L2 5l3 3" fill="none" stroke="#111" stroke-width="1.3"/></svg></div>

<div class="event" style="left:259px"><div class="img" style="background:linear-gradient(135deg,#efe8da,#b07040 55%,#2a2018)" role="img" aria-label="Open bible with a wooden crucifix"></div><h4 class="slab">Person Of Jesus Christ Of Love</h4><div class="meta"><span><i></i>June 28, 2021</span><span>|</span><span><i></i>5 Comments</span></div></div>
<div class="event" style="left:496px"><div class="img" style="background:linear-gradient(135deg,#d9c27a,#7c8a48 55%,#3a3f22)" role="img" aria-label="Woman praying among trees"></div><h4 class="slab">Love Reborn As The Lord</h4><div class="meta"><span><i></i>June 28, 2021</span><span>|</span><span><i></i>5 Comments</span></div></div>
<div class="event" style="left:733px"><div class="img" style="background:linear-gradient(135deg,#6a6a70,#1d1d22 60%,#0c0c10)" role="img" aria-label="Crowd raising hands during worship"></div><h4 class="slab">All Think With God's Children</h4><div class="meta"><span><i></i>June 28, 2021</span><span>|</span><span><i></i>5 Comments</span></div></div>

<!-- CTA -->
<div class="cta">
  <h3 class="abs slab" style="left:246px;top:24px;font-size:21px;font-weight:600;color:var(--ink)">Not A Member? Connect With Us..</h3>
  <div class="abs slab" style="left:785px;top:18px;width:169px;height:34px;background:var(--ink);color:#fff;font-size:9px;display:flex;align-items:center;justify-content:center">CONNECT WITH US</div>
</div>

<!-- FOOTER -->
<footer>
  <div class="abs footer-col" style="left:252px;top:4490px;width:200px">
    <h4 class="slab">About Us</h4>
    <p>"Lorem ipsum dolor sit amet, consectetur adipiscing elit, sed do eiusmod tempor in cididunt ut labore et dolore</p>
    <p style="margin-top:8px">"Lorem ipsum dolor sit amet, consectetur adipiscing elit, sed do eiusmod tempor in cididunt ut laboreing <span style="color:var(--gold)">Read more</span></p>
  </div>
  <div class="abs footer-col" style="left:550px;top:4490px">
    <h4 class="slab">Quick Links</h4>
    <ul><li>About Me</li><li>Contact Me</li><li>Blog</li><li>Our Reviews</li><li>Privacy Policy</li><li>Terms</li></ul>
  </div>
  <div class="abs footer-col" style="left:729px;top:4490px;width:220px">
    <h4 class="slab">Subscribe Newsletter</h4>
    <div class="field"><span>Your Name</span><svg width="9" height="9" viewBox="0 0 9 9"><circle cx="4.5" cy="4.5" r="3.5" fill="none" stroke="#111"/></svg></div>
    <div class="field"><span>Your Email</span><svg width="10" height="8" viewBox="0 0 10 8"><rect x=".5" y=".5" width="9" height="7" fill="none" stroke="#111"/><path d="M.5.5l4.5 4 4.5-4" fill="none" stroke="#111"/></svg></div>
    <div class="btn" style="margin-left:150px;width:70px;height:28px;font-size:8px">SUBSCRIBE</div>
  </div>
  <div class="abs" style="left:252px;top:4668px;width:698px;height:1px;background:var(--line)"></div>
  <div class="abs" style="left:254px;top:4690px"><span class="social"></span><span class="social"></span><span class="social"></span><span class="social"></span></div>
  <p class="abs" style="left:806px;top:4697px;font-size:8px;color:var(--ink)">© Gracefield 2021 All Rights Reserved</p>
  <div class="abs" style="left:1152px;top:4640px;width:24px;height:22px;background:var(--gold);display:flex;align-items:center;justify-content:center"><svg width="10" height="10" viewBox="0 0 10 10"><path d="M5 9V2M2 5l3-3 3 3" fill="none" stroke="#111" stroke-width="1.3"/></svg></div>
</footer>

</body>
</html>
```